Corporate Design für Sanitär Heizungs - und Klima Unternehmen
Zielgruppe
Wir sind ein Fachfirma mit einer Familien History von über 70 Jahren und unserem Landkreis vertreten. Wir verkaufen eher hochpreisige Lösungen an unsere Kunden.
Santiär & heizungstechnische Anlage konventioneller und regenerativer Art sowie komplette Trinkwasseranlagen der obersten Güte.
Unsere Zielgruppen sind Privatpersonen, Wohngemeinschaften, Hausverwaltungen & technische Anlagen jeglicher Unternehmen.
Aufgabenstellung
Bisher wurde vereinzelt Motive und Idee gesammelt umgesetzt. Gerne kann sich daran orientiert oder diese nochmal komplett überarbeitet werden. Unsere aktuellen Farben sind fastdie selben.
Wir sind aber bereit für neue Anreize und Vorstellungen da sich das Unternehmen gerade im Umbruch finder durch eine Geschäftsübergabe an die jüngere Generation.
Gerne hätten wir auch eine Mail Signatur. Wahlweise als Vorlage damit wir es auf die einzelnen Sachbearbeiter abstimmen können.

```html
<!DOCTYPE html>
<html lang="de">
<head>
<meta charset="utf-8">
<title>Walden Heizungsbau – Visitenkarte</title>
<link href="https://fonts.googleapis.com/css2?family=PT+Serif:wght@400;700&display=swap" rel="stylesheet">
<style>
  :root {
    --bg: #e6e6e6;
    --card: #fafafa;
    --teal: #13909c;
    --orange: #f0992e;
    --slate: #626363;
    --mist: #eef0ed;
    --text: #555657;
  }
  * { margin: 0; padding: 0; box-sizing: border-box; }
  html, body { width: 1200px; height: 1200px; overflow: hidden; }
  body { background: var(--bg); font-family: "PT Serif", Georgia, serif; position: relative; }

  .card {
    position: absolute; left: 221px; width: 758px; height: 433px;
    background: var(--card);
    box-shadow: 0 1px 3px rgba(0,0,0,.06);
  }
  .card--front { top: 104px; }
  .card--back { top: 662px; }
  .card .stripes { position: absolute; inset: 0; width: 100%; height: 100%; }

  .brand {
    position: absolute; display: flex; align-items: center;
    color: var(--slate); font-weight: 700; white-space: nowrap; line-height: 1;
  }
  .brand__dot { border-radius: 50%; background: var(--teal); flex: none; }

  .card--front .brand { left: 0; right: 0; top: 200px; justify-content: center; gap: 16px; font-size: 32px; }
  .card--front .brand__dot { width: 28px; height: 28px; }

  .card--back .brand--large { left: 96px; top: 202px; gap: 10px; font-size: 20px; }
  .card--back .brand--large .brand__dot { width: 16px; height: 16px; }

  .divider {
    position: absolute; left: 358px; top: 100px; width: 14px; height: 275px;
    background: radial-gradient(ellipse at left center, rgba(70,90,110,.22), rgba(70,90,110,0) 70%);
  }

  .card--back .brand--small { left: 400px; top: 170px; gap: 7px; font-size: 15px; }
  .card--back .brand--small .brand__dot { width: 10px; height: 10px; }

  .contact { position: absolute; left: 398px; top: 225px; list-style: none; }
  .contact li { display: flex; align-items: center; height: 34.5px; font-size: 18.5px; color: var(--text); }
  .contact svg { width: 20px; height: 20px; margin-right: 12px; flex: none; }
</style>
</head>
<body>

<section class="card card--front">
  <svg class="stripes" viewBox="0 0 784 448" preserveAspectRatio="none" aria-hidden="true">
    <polygon fill="var(--orange)" points="0,0 240,0 226,25 0,25"/>
    <polygon fill="var(--slate)" points="240,0 257,0 243,25 226,25"/>
    <polygon fill="var(--mist)" points="257,0 322,0 308,25 243,25"/>
    <polygon fill="var(--teal)" points="322,0 508,0 492,25 308,25"/>
    <polygon fill="var(--teal)" points="20,413 380,413 358,448 0,448"/>
    <polygon fill="var(--mist)" points="380,413 505,413 483,448 358,448"/>
    <polygon fill="var(--slate)" points="505,413 541,413 519,448 483,448"/>
    <polygon fill="var(--orange)" points="541,413 784,413 784,448 519,448"/>
  </svg>
  <div class="brand"><span class="brand__dot"></span>Walden Heizungsbau</div>
</section>

<section class="card card--back">
  <svg class="stripes" viewBox="0 0 784 448" preserveAspectRatio="none" aria-hidden="true">
    <polygon fill="var(--teal)" points="20,413 380,413 358,448 0,448"/>
    <polygon fill="var(--mist)" points="380,413 505,413 483,448 358,448"/>
    <polygon fill="var(--slate)" points="505,413 541,413 519,448 483,448"/>
    <polygon fill="var(--orange)" points="541,413 784,413 784,448 519,448"/>
  </svg>

  <div class="brand brand--large"><span class="brand__dot"></span>Walden Heizungsbau</div>
  <div class="divider"></div>
  <div class="brand brand--small"><span class="brand__dot"></span>Walden Heizungsbau</div>

  <ul class="contact">
    <li>
      <svg viewBox="0 0 20 20"><path fill="var(--slate)" d="M10 1a6 6 0 0 0-6 6c0 4.5 6 12 6 12s6-7.5 6-12a6 6 0 0 0-6-6zm0 8.3A2.3 2.3 0 1 1 10 4.7a2.3 2.3 0 0 1 0 4.6z"/></svg>
      Brunnenweg 12, 40210 Düsseldorf
    </li>
    <li>
      <svg viewBox="0 0 20 20"><path fill="var(--slate)" d="M14.5 2.5l2.5 2.2-1.7 2.1-2.2-1.2c-2.6 1.6-5 4.5-6.2 7.5l1.6 1.9-1.8 2-2.6-1.9C4.9 10.2 9 4.6 14.5 2.5z"/></svg>
      +49 151 203 118 47
    </li>
    <li>
      <svg viewBox="0 0 20 20"><rect x="2" y="5" width="16" height="11" fill="none" stroke="var(--slate)" stroke-width="1.4"/><path d="M2 5l8 6 8-6M2 16l6-5M18 16l-6-5" fill="none" stroke="var(--slate)" stroke-width="1.2"/></svg>
      info@walden-wt.de
    </li>
    <li>
      <svg viewBox="0 0 20 20"><g fill="none" stroke="var(--slate)" stroke-width="1.1"><circle cx="10" cy="10" r="8"/><ellipse cx="10" cy="10" rx="3.5" ry="8"/><path d="M2 10h16M3.5 6h13M3.5 14h13"/></g></svg>
      www.walden-wt.de
    </li>
  </ul>
</section>

</body>
</html>
```